Luísa Tavares Arquitetura e Urbanismo precisa do Design de uma Página em Revista de Negócios

Preciso do design de uma página para publicar em uma revista de negócios, para Marketing, visando a expansão do meu serviço de Fortaleza para a região Centro-Sul do estado do Ceará. Trabalho com projetos de ambientação, bem como projeto arquitetônicos residenciais e comerciais. A página da revista tem dimensões de 21,5cm x 30,5cm e deve apresentar layout sofisticado e clean, usando tons de amarelo mostarda e branco, se assemelhando com a ideia da Revista Pirilampo (Fortaleza) e Nível Um. O projeto final deve comunicar sofisticação e confiança de que tenho a oferecer o que há de mais atual no mercado, trabalhando sempre a ideia da personalização.

```html
<!DOCTYPE html>
<html lang="pt-BR">
<head>
<meta charset="UTF-8">
<title>Luísa Tavares Arquitetura e Urbanismo — Página de Revista</title>
<link rel="stylesheet" href="https://fonts.googleapis.com/css2?family=Didact+Gothic&family=Montserrat:wght@600;700&display=swap">
<style>
  :root {
    --backdrop: #2b2826;
    --paper: #f7f6ec;
    --sand-light: #eeeedd;
    --sand-mid: #dcdcc2;
    --ink-grey: #6d6e70;
    --mustard: #b9b43a;
    --teal: #4f7a6e;
    --band-grey: #4d4d4f;
    --brand-yellow: #f1e21c;
    --white: #ffffff;
  }
  * { margin: 0; padding: 0; box-sizing: border-box; }
  html, body {
    width: 1200px; height: 1000px; overflow: hidden;
    background: var(--backdrop);
  }
  .magazine-page {
    position: absolute; left: 276px; top: 41px;
    width: 648px; height: 918px;
    background: var(--paper); overflow: hidden;
  }
  .dune-backdrop {
    position: absolute; inset: 0 0 260px 0;
    background:
      radial-gradient(ellipse 70% 18% at 40% 22%, rgba(255,255,255,.8), transparent 70%),
      radial-gradient(ellipse 60% 14% at 70% 45%, rgba(255,255,255,.7), transparent 70%),
      linear-gradient(180deg, var(--sand-mid) 0%, var(--sand-light) 40%, var(--paper) 100%);
  }
  .brand-name {
    position: absolute; top: 176px; width: 100%; text-align: center;
    font-family: "Didact Gothic", sans-serif; font-size: 26px;
    color: var(--brand-yellow); letter-spacing: 1px;
  }
  .headline { position: absolute; top: 228px; width: 100%; text-align: center; }
  .headline-light {
    font-family: "Didact Gothic", sans-serif; font-size: 50px;
    color: var(--ink-grey); line-height: 44px; letter-spacing: -0.5px;
  }
  .headline-bold {
    font-family: "Montserrat", sans-serif; font-weight: 700;
    font-size: 58px; line-height: 66px; letter-spacing: -1px;
  }
  .headline-bold.residential { color: var(--mustard); margin-top: 14px; }
  .headline-bold.commercial { color: var(--teal); }
  .footer-band {
    position: absolute; left: 0; right: 0; bottom: 0; height: 260px;
    background: var(--band-grey);
  }
  .project-render {
    position: absolute; border: 1px solid #9a9a9a; border-radius: 3px;
  }
  .render-store { left: 30px; top: 570px; width: 157px; height: 156px;
    background: linear-gradient(160deg, #e3b13a 0%, #d9d6cf 45%, #3b4a4f 100%); }
  .render-office { left: 155px; top: 543px; width: 213px; height: 212px;
    background: linear-gradient(180deg, #cfcac2 0%, #e9e7e3 55%, #d8c25a 100%); }
  .render-study { left: 348px; top: 511px; width: 158px; height: 123px;
    background: linear-gradient(170deg, #e5e2dc 0%, #4f9a93 60%, #3a3b40 100%); }
  .render-garden { left: 464px; top: 603px; width: 157px; height: 157px;
    background: linear-gradient(180deg, #6f8fb4 0%, #d7d7d2 40%, #3f6d2c 100%); }
  .render-bedroom { left: 316px; top: 636px; width: 155px; height: 156px;
    background: linear-gradient(170deg, #d8d5cf 0%, #2c3550 50%, #c98a3a 100%); }
  .studio-signature {
    position: absolute; left: 18px; bottom: 12px;
    font-family: "Didact Gothic", sans-serif; font-size: 16px; color: var(--white);
  }
  .studio-signature .studio-name {
    font-family: "Montserrat", sans-serif; font-weight: 700; font-size: 18px;
    color: var(--brand-yellow); margin-right: 8px;
  }
</style>
</head>
<body>
  <main class="magazine-page">
    <div class="dune-backdrop" role="img" aria-label="Vista aérea esmaecida de dunas e litoral em tons de areia"></div>

    <div class="brand-name">Luísa Tavares</div>

    <h1 class="headline">
      <div class="headline-light">projeto</div>
      <div class="headline-light">arquitetônicos</div>
      <div class="headline-bold residential">residenciais e</div>
      <div class="headline-bold commercial">comerciais</div>
    </h1>

    <div class="footer-band"></div>

    <div class="project-render render-store" role="img" aria-label="Render de loja com teto amarelo e estantes de produtos"></div>
    <div class="project-render render-office" role="img" aria-label="Render de escritório com bancada branca e cadeiras amarelas"></div>
    <div class="project-render render-study" role="img" aria-label="Render de home office com estante azul-petróleo"></div>
    <div class="project-render render-garden" role="img" aria-label="Render de fachada residencial com jardim e palmeira"></div>
    <div class="project-render render-bedroom" role="img" aria-label="Render de quarto com parede azul-marinho e poltrona laranja"></div>

    <p class="studio-signature"><span class="studio-name">Luísa Tavares</span>Arquitetura e Urbanismo</p>
  </main>
</body>
</html>
```